Cafe Menu Required

We need a menu for our coffee shop.
I would like something very much the same as what I have attached.

I have attached a word doc with the items needed on the menu.

I have also attached our logo

I would like to print these on A3 size poster

Industry/Entity Type

Cafe

```html
<!DOCTYPE html>
<html lang="en">
<head>
<meta charset="utf-8">
<title>Ward Cafe Menu</title>
<link rel="stylesheet" href="https://fonts.googleapis.com/css2?family=Crimson+Pro:wght@400;600&family=Josefin+Sans:wght@400;600&display=swap">
<style>
  :root {
    --bg-deep: #1f0f25;
    --bg-mid: #3b2144;
    --bg-glow: #4a2b55;
    --gold: #f2cf5b;
    --gold-dark: #a9822e;
    --gold-light: #fbe9a6;
    --text: #f4eff6;
    --white: #ffffff;
  }
  * { margin: 0; padding: 0; box-sizing: border-box; }
  html, body { width: 850px; height: 1200px; overflow: hidden; background: var(--bg-deep); }
  .menu {
    position: relative;
    width: 850px;
    height: 1200px;
    overflow: hidden;
    font-family: "Crimson Pro", Georgia, serif;
    color: var(--text);
  }
  .menu-backdrop {
    position: absolute; inset: 0;
    background: radial-gradient(ellipse at 50% 45%, var(--bg-glow) 0%, var(--bg-mid) 40%, var(--bg-deep) 100%);
  }
  .brand {
    position: absolute; top: 82px; left: 0; width: 850px;
    text-align: center;
  }
  .brand-name {
    font-family: "Josefin Sans", Arial, sans-serif;
    font-weight: 600; font-size: 52px; color: var(--white); line-height: 1;
  }
  .tagline {
    position: absolute; top: 196px; left: 0; width: 850px; text-align: center;
    font-family: "Josefin Sans", Arial, sans-serif;
    font-size: 31px; font-weight: 400; color: var(--white); letter-spacing: 0.3px;
  }
  .tagline-sep {
    display: inline-block; width: 9px; height: 9px; border-radius: 50%;
    background: var(--gold); margin: 0 14px; vertical-align: middle;
  }
  .header-rule {
    position: absolute; top: 247px; left: 0; width: 850px; height: 4px;
    background: linear-gradient(90deg, var(--gold-dark), var(--gold-light) 50%, var(--gold-dark));
  }
  .footer-band {
    position: absolute; bottom: 0; left: 0; width: 850px; height: 24px;
    background: linear-gradient(90deg, var(--gold-dark), var(--gold-light) 35%, var(--gold) 60%, var(--gold-dark));
  }
  .section { position: absolute; left: 149px; width: 560px; }
  .section-title {
    font-size: 21px; font-weight: 400; color: var(--gold); text-decoration: underline;
    text-underline-offset: 3px; line-height: 26px; margin-bottom: 26px;
  }
  .item { display: flex; font-size: 21px; line-height: 26px; }
  .item-name { width: 436px; }
  .section--cold .item-name { width: 439px; }
  .item-price { color: var(--gold); }
  .section--hot { top: 265px; }
  .section--extras { top: 732px; }
  .section--cold { top: 940px; }
</style>
</head>
<body>
<main class="menu">
  <div class="menu-backdrop" role="img" aria-label="Dark purple background with a faint swirling damask pattern"></div>

  <header>
    <div class="brand">
      <span class="brand-name">Ward Cafe</span>
    </div>
    <p class="tagline">Coffee<span class="tagline-sep"></span>Catering<span class="tagline-sep"></span>Food to go</p>
    <div class="header-rule"></div>
  </header>

  <section class="section section--hot">
    <h2 class="section-title">HOT BEVERAGES</h2>
    <div class="item"><span class="item-name">Espresso</span><span class="item-price">3.5</span></div>
    <div class="item"><span class="item-name">Piccolo</span><span class="item-price">3.5</span></div>
    <div class="item"><span class="item-name">Short Macchiato</span><span class="item-price">4.0</span></div>
    <div class="item"><span class="item-name">Long Macchiato</span><span class="item-price">4.5</span></div>
    <div class="item"><span class="item-name">Latte</span><span class="item-price">4/4.5/5.5</span></div>
    <div class="item"><span class="item-name">Cappucinno</span><span class="item-price">4/4.5/5.5</span></div>
    <div class="item"><span class="item-name">Flat White</span><span class="item-price">4/4.50/5.50</span></div>
    <div class="item"><span class="item-name">Long Black</span><span class="item-price">4/4.50/5.50</span></div>
    <div class="item"><span class="item-name">Hot Chocolate</span><span class="item-price">4/4.50/5.50</span></div>
    <div class="item"><span class="item-name">White Hot Chocolate</span><span class="item-price">4/4.50/5.50</span></div>
    <div class="item"><span class="item-name">Mocha</span><span class="item-price">4.5/5.0/6.0</span></div>
    <div class="item"><span class="item-name">White Choc Mocha</span><span class="item-price">4.5/5.0/6.0</span></div>
    <div class="item"><span class="item-name">Chai Latte</span><span class="item-price">4.5/5.0/6.0</span></div>
    <div class="item"><span class="item-name">Dirty Chai</span><span class="item-price">5.0/5.5/6.5</span></div>
    <div class="item"><span class="item-name">Selection of Teas</span><span class="item-price">3.8</span></div>
  </section>

  <section class="section section--extras">
    <h2 class="section-title">EXTRAS</h2>
    <div class="item"><span class="item-name">Extra Shot</span><span class="item-price">0.5</span></div>
    <div class="item"><span class="item-name">Decaf</span><span class="item-price">0.5</span></div>
    <div class="item"><span class="item-name">Syrups – Caramel/Hazelnut/Vanilla</span><span class="item-price">0.5</span></div>
    <div class="item"><span class="item-name">Soy</span><span class="item-price">0.5</span></div>
    <div class="item"><span class="item-name">Lactose free</span><span class="item-price">0.5</span></div>
  </section>

  <section class="section section--cold">
    <h2 class="section-title">COLD BEVERAGES</h2>
    <div class="item"><span class="item-name">Iced Latte</span><span class="item-price">4.5</span></div>
    <div class="item"><span class="item-name">Iced Long Black</span><span class="item-price">4.5</span></div>
    <div class="item"><span class="item-name">Iced Coffee w/ice cream</span><span class="item-price">6.0</span></div>
    <div class="item"><span class="item-name">Iced Chocolate w/ice cream</span><span class="item-price">6.0</span></div>
    <div class="item"><span class="item-name">Coffee Frappe</span><span class="item-price">6.0</span></div>
    <div class="item"><span class="item-name">Mango Frappe</span><span class="item-price">6.0</span></div>
  </section>

  <div class="footer-band"></div>
</main>
</body>
</html>
```